DeedVault Site Introduction and overview Flyer

We need a flyer made that gives an over view of our business. We are a land and mineral records company based in Texas that provides data to many different industries. This should be a bi-fold flyer that measures a 6" x 6" square. The designs should incorporate our company colors with subtle uses of the brighter colors from our new website. Logo and new website pictures are uploaded below.
we would like for the inside left to contain a brief company description: " Since 2005, DeedVault has provided online access to courthouse records and mineral ownership data. Our data, search and order management tools allow you to quickly build and store chains of title, division orders and contact lists. No other website provides as comprehensive of a data set. Start searching DeedVault today.
The front should contain a relevant photo, logo and website name.
the back should contain our contact information and graphic.
the inside right should contain 5 major bullet points with appropriate icons. the bullet points will be:
1. County Courthouse Records Available in Texas, Colorado, New Mexico, and Oklahoma
2. Search all Texas counties at once with Broadscan Lookup
3. Search mineral ownership data from across the State of Texas
4. Download bulk mineral appraisal rolls
5. Plats available in select counties

Target Market(s)
Oil & Gas, Legal, Surveyors, Title, Real Estate, male and female
Industry/Entity Type
Business
Font styles to use
Colors
Designer to choose colors to be used in the design.
Requirements
Must have
- Simplicity.
- relevant colors/graphics

Nice to have
- we would like to have the graphic shown in the sitecapture 2 used, if possible

Should not have
- non-relevant colors, graphics

```html
<!DOCTYPE html>
<html lang="en">
<head>
<meta charset="utf-8">
<title>DeedVault Bi-fold Flyer</title>
<link href="https://fonts.googleapis.com/css2?family=Lato:wght@400;700&family=Roboto+Condensed:wght@400;700&display=swap" rel="stylesheet">
<style>
  :root {
    --navy: #2b2a6e;
    --brand-blue: #1f3a93;
    --cyan: #27b6d6;
    --charcoal: #333438;
    --ink: #2a2a2a;
    --paper: #ffffff;
    --stage: #ececec;
  }
  html, body { margin: 0; padding: 0; width: 1200px; height: 1200px; overflow: hidden; background: var(--stage); }
  .spread { position: absolute; left: 0; top: 304px; width: 1200px; height: 592px; background: var(--paper); overflow: hidden; box-shadow: 0 4px 14px rgba(0,0,0,.18); }
  .spread-shapes { position: absolute; inset: 0; }
  .back-panel { position: absolute; left: 25px; top: 0; width: 400px; font-family: 'Lato', sans-serif; color: var(--ink); }
  .section-title { position: absolute; left: 0; margin: 0; font: 700 13px 'Lato', sans-serif; color: var(--brand-blue); letter-spacing: .1px; }
  .welcome-title { top: 148px; }
  .intro { position: absolute; left: 0; top: 176px; width: 386px; margin: 0; font-size: 11.6px; line-height: 15px; text-align: justify; }
  .contact-title { top: 325px; }
  .contact-group { position: absolute; left: 0; width: 400px; }
  .contact-group.billing { top: 352px; }
  .contact-group.shipping { top: 457px; }
  .group-label { margin: 0 0 7px; font: 700 12.5px 'Lato', sans-serif; color: #333; }
  .contact-line { display: flex; align-items: center; gap: 7px; margin: 0 0 7px; font-size: 11.5px; height: 16px; }
  .contact-line svg { width: 11px; height: 11px; fill: #444; flex: none; }
  .brand-name { position: absolute; font-family: 'Roboto Condensed', sans-serif; font-weight: 700; color: var(--brand-blue); display: flex; align-items: center; gap: 7px; margin: 0; }
  .brand-mark { background: var(--brand-blue); flex: none; }
  .back-brand { left: 323px; top: 424px; font-size: 26px; }
  .back-brand .brand-mark { width: 14px; height: 14px; }
  .web-tab { position: absolute; left: 24px; top: 568px; font: 400 12px 'Lato', sans-serif; color: #fff; display: flex; align-items: center; gap: 6px; }
  .web-tab svg { width: 11px; height: 11px; fill: none; stroke: #fff; stroke-width: 1.4; }
  .front-brand { left: 622px; top: 262px; font-size: 30px; }
  .front-brand .brand-mark { width: 16px; height: 16px; }
  .front-copy { position: absolute; left: 622px; font-family: 'Roboto Condensed', sans-serif; margin: 0; }
  .tagline-accent { color: var(--cyan); font-weight: 400; font-size: 22px; line-height: 24px; }
  .tagline-main { color: #fff; font-weight: 700; font-size: 21px; line-height: 24px; }
  .tagline-sub { color: #fff; font-weight: 400; font-size: 17px; line-height: 20px; }
  .tag-one { top: 358px; }
  .tag-two { top: 432px; }
  .front-phone { position: absolute; left: 622px; top: 523px; display: flex; align-items: center; gap: 8px; font: 400 21px 'Roboto Condensed', sans-serif; color: #fff; }
  .front-phone svg { width: 20px; height: 20px; fill: none; stroke: #fff; stroke-width: 1.6; }
  .front-web { position: absolute; left: 626px; top: 572px; font: 400 12px 'Lato', sans-serif; letter-spacing: 5px; color: #444; }
</style>
</head>
<body>
<main class="spread">
  <svg class="spread-shapes" viewBox="0 0 1200 592" width="1200" height="592" aria-hidden="false">
    <defs>
      <linearGradient id="sky" x1="0" y1="0" x2="0" y2="1">
        <stop offset="0" stop-color="#2d4f9c"/>
        <stop offset=".35" stop-color="#6b86c0"/>
        <stop offset=".55" stop-color="#d98a5c"/>
        <stop offset=".75" stop-color="#6b5a48"/>
        <stop offset="1" stop-color="#2b2a30"/>
      </linearGradient>
      <linearGradient id="curl" x1="0" y1="0" x2="1" y2="0">
        <stop offset="0" stop-color="#c9cacd"/>
        <stop offset=".4" stop-color="#f4f4f5"/>
        <stop offset="1" stop-color="#ffffff"/>
      </linearGradient>
      <linearGradient id="backWash" x1="0" y1="0" x2="1" y2="0">
        <stop offset="0" stop-color="#ffffff"/>
        <stop offset="1" stop-color="#f1f2f4"/>
      </linearGradient>
    </defs>

    <rect class="back-wash" x="0" y="0" width="600" height="592" fill="url(#backWash)"/>

    <polygon class="cover-photo" role="img" aria-label="Photo of an oil refinery with lit towers against a dusk sky" points="785,0 1200,0 1200,592 905,592" fill="url(#sky)"/>

    <polygon class="navy-band" points="370,0 700,0 912,576 584,592" fill="var(--navy)"/>
    <line x1="362" y1="0" x2="578" y2="592" stroke="var(--cyan)" stroke-width="4"/>
    <line x1="692" y1="0" x2="904" y2="576" stroke="var(--cyan)" stroke-width="4"/>
    <line x1="600" y1="0" x2="600" y2="592" stroke="rgba(0,0,0,.12)" stroke-width="1"/>

    <polygon class="dark-notch" points="682,0 785,0 733,118" fill="var(--charcoal)"/>
    <polygon class="dark-wedge" points="486,313 584,592 460,592" fill="var(--charcoal)"/>

    <polygon class="ribbon-curl" points="419,168 600,179 600,308 468,308 448,260" fill="url(#curl)"/>
    <polygon class="ribbon-block" points="600,179 760,179 805,308 600,308" fill="#ffffff"/>

    <polygon class="front-footer" points="569,560 912,560 919,592 579,592" fill="#ffffff"/>
    <rect class="accent-rule" x="919" y="586" width="281" height="6" fill="var(--cyan)"/>

    <polygon class="web-tab-shape" points="0,566 177,566 168,592 0,592" fill="var(--charcoal)"/>
  </svg>

  <section class="back-panel">
    <h2 class="section-title welcome-title">WELCOME TO DEEDVAULT.COM</h2>
    <p class="intro">DeedVault LLC was started in 2005 as a division of a large independent title insurance agency based in Corpus Christi, Texas. Our parent company Bayline Title has been providing Texas land research and title insurance for over 50 years. Several counties on DeedVault.com are licensed title plants used to underwrite title insurance by major underwriters.</p>

    <h2 class="section-title contact-title">CONTACT DETAILS:</h2>
    <div class="contact-group billing">
      <p class="group-label">Accounting and billing inquiries</p>
      <p class="contact-line"><svg viewBox="0 0 12 12"><path d="M6 1 0 6h1.6v5h3V8h2.8v3h3V6H12z"/></svg>418 Harbor St., Corpus Christi, TX 78401</p>
      <p class="contact-line"><svg viewBox="0 0 12 12"><path d="M0 3h12v7H0zM1 4l5 3.5L11 4"/></svg>mark@deedvault.com</p>
      <p class="contact-line"><svg viewBox="0 0 12 12"><path d="M3 1 1.5 2.5c0 5 3 8 8 8L11 9 8.8 7.3 7.6 8.4C5.8 7.6 4.4 6.2 3.6 4.4L4.7 3.2z"/></svg>(214) 555-0142</p>
    </div>
    <div class="contact-group shipping">
      <p class="group-label">Shipping address</p>
      <p class="contact-line"><svg viewBox="0 0 12 12"><path d="M6 1 0 6h1.6v5h3V8h2.8v3h3V6H12z"/></svg>7700 Meadow Pkwy, Suite 310, Frisco, TX 75035</p>
      <p class="contact-line"><svg viewBox="0 0 12 12"><path d="M0 3h12v7H0zM1 4l5 3.5L11 4"/></svg>info@deedvault.com</p>
      <p class="contact-line"><svg viewBox="0 0 12 12"><path d="M3 1 1.5 2.5c0 5 3 8 8 8L11 9 8.8 7.3 7.6 8.4C5.8 7.6 4.4 6.2 3.6 4.4L4.7 3.2z"/></svg>(214) 555-0142</p>
    </div>
  </section>

  <p class="brand-name back-brand"><span class="brand-mark"></span>DeedVault</p>
  <div class="web-tab"><svg viewBox="0 0 12 12"><circle cx="6" cy="6" r="5"/><path d="M1 6h10M6 1c2.5 3 2.5 7 0 10M6 1c-2.5 3-2.5 7 0 10"/></svg>www.deedvault.com</div>

  <p class="brand-name front-brand"><span class="brand-mark"></span>DeedVault</p>
  <p class="front-copy tag-one"><span class="tagline-accent">Land and mineral</span><br><span class="tagline-main">RECORDS COMPANY</span></p>
  <p class="front-copy tag-two"><span class="tagline-accent" style="font-weight:700">We provides data</span><br><span class="tagline-sub">to many different industries</span></p>
  <div class="front-phone"><svg viewBox="0 0 20 20"><circle cx="10" cy="10" r="9"/><path d="M7 5 5.8 6.2c0 4.5 3.5 8 8 8L15 13l-1.8-1.5-1.1 1c-1.6-.7-2.8-1.9-3.5-3.5l1-1.1z"/></svg>(214) 555-0142</div>
  <div class="front-web">www.deedvault.com</div>
</main>
</body>
</html>
```